I'm looking for a book cover with the Main title:
Quiet Mornings Along the Misty Coastal Lighthouse Trail

Subtitle: The Wanderer's Journal of Seaside Rambles

Looking for a clean design that attracts people to the book.

Open to all styles of design (plain text, animated characters, scenery) as long as the text is in basic font and easy to read.

This is to be put somewhere under the titles
Written By: Veselin Markhov

The back of the book will have:

"A physical, mental, emotional, and spiritual guide to fat loss. Going beyond calorie deficit diets and working out for hours a day in order to achieve results. It will help you get to the root cause of weight gain and give you the tools you need to take charge of your health and your life.

You will learn:
- The Best Foods to Eat for Fat Loss
- The Foods You Need to Avoid
- How to Heal Your Hormones
- Strategies to Overcome Emotional Eating
- Mindset and Motivation Tactics
- How to Meditate Without Losing Your Mind

I created this book to help those struggling with losing fat in a healthy, holistic, and sustainable way. It’s my sincere hope that this book gives you what you need in order to achieve your goals. "

Please place the photo somewhere on the back as well if it fits with the design.

Thank you for your time!

```html
<!DOCTYPE html>
<html lang="en">
<head>
<meta charset="utf-8">
<title>Quiet Mornings Along the Misty Coastal Lighthouse Trail — Book Cover</title>
<link rel="stylesheet" href="https://fonts.googleapis.com/css2?family=Montserrat:wght@300;700;800&family=Bilbo+Swash+Caps&display=swap">
<style>
  :root {
    --paper: #e9e9e9;
    --sky: #55b4e0;
    --berry: #cc2866;
    --ink: #1a1a1a;
  }
  html, body {
    margin: 0;
    padding: 0;
    overflow: hidden;
    background: var(--paper);
  }
  .cover {
    position: relative;
    width: 802px;
    height: 1200px;
    overflow: hidden;
    background: var(--paper);
  }
  .cover__art {
    position: absolute;
    inset: 0;
    width: 802px;
    height: 1200px;
  }
  .title-line {
    font-family: "Montserrat", sans-serif;
    font-weight: 800;
    letter-spacing: -2px;
  }
  .title-line--sky { fill: var(--sky); }
  .title-line--berry { fill: var(--berry); }
  .title-line__light { font-weight: 300; }
  .author {
    font-family: "Bilbo Swash Caps", cursive;
    fill: var(--ink);
    font-size: 64px;
  }
  .subtitle-band { fill: var(--sky); }
  .subtitle {
    font-family: "Montserrat", sans-serif;
    font-weight: 700;
    font-size: 25px;
    fill: var(--berry);
    letter-spacing: 0.2px;
  }
</style>
</head>
<body>
  <main class="cover">
    <svg class="cover__art" viewBox="0 0 802 1200" xmlns="http://www.w3.org/2000/svg">
      <g class="title">
        <text class="title-line title-line--sky" x="0" y="118" font-size="128">QUIET</text>
        <text class="title-line title-line--berry" x="0" y="262" font-size="124" letter-spacing="-4">MORN<tspan class="title-line__light">INGS</tspan></text>
        <text class="title-line title-line--berry" x="0" y="395" font-size="112">ALONG THE</text>
        <text class="title-line title-line--sky" x="0" y="545" font-size="148">MISTY</text>
        <text class="title-line title-line--sky" x="0" y="690" font-size="140">COASTAL</text>
        <text class="title-line title-line--sky" x="0" y="825" font-size="104">LIGHTHOUSE</text>
        <text class="title-line title-line--sky" x="-4" y="1066" font-size="212">TRAIL</text>
      </g>

      <g class="author-credit" transform="rotate(-22 660 960)">
        <text class="author" x="540" y="940">Veselin</text>
        <text class="author" x="580" y="1005">Markhov</text>
      </g>

      <rect class="subtitle-band" x="0" y="1088" width="802" height="112"/>
      <text class="subtitle" x="401" y="1148" text-anchor="middle">THE WANDERER'S JOURNAL OF SEASIDE RAMBLES</text>
    </svg>
  </main>
</body>
</html>
```